Brindlemark Services Ltd

I'd like to create a company letterhead for the attached logo in word format.

I'd like to emphasis the icon in large translucent state from the left corner and ensure that the letterhead colouring matches the colour palette of the current logo with a contrast so it's clear to see. I've attached a copy of our sister company page on the app for reference.

```html
<!DOCTYPE html>
<html lang="en">
<head>
<meta charset="utf-8">
<title>Brindlemark Services Ltd — Letterhead</title>
<link href="https://fonts.googleapis.com/css2?family=Nunito:wght@400;500&display=swap" rel="stylesheet">
<style>
  :root {
    --backdrop: #66686c;
    --paper: #f2f2f2;
    --brand-teal: #4db8a4;
    --teal-faint: #dce9e7;
    --ink: #4a4d52;
  }
  html, body {
    margin: 0;
    padding: 0;
    width: 1200px;
    height: 803px;
    overflow: hidden;
    background: var(--backdrop);
    font-family: "Nunito", sans-serif;
  }
  .letterhead {
    position: absolute;
    left: 330px;
    top: 20px;
    width: 541px;
    height: 763px;
    background: linear-gradient(135deg, #f6f6f6 0%, var(--paper) 50%, #ececec 100%);
    overflow: hidden;
    border-bottom: 1.5px solid var(--brand-teal);
    box-sizing: border-box;
  }
  .brand {
    position: absolute;
    left: 51px;
    top: 46px;
    display: flex;
    align-items: center;
    gap: 8px;
  }
  .brand-dot {
    width: 28px;
    height: 28px;
    border-radius: 50%;
    background: var(--brand-teal);
  }
  .brand-name {
    font-size: 19px;
    font-weight: 400;
    color: var(--brand-teal);
    line-height: 1;
  }
  .contact {
    position: absolute;
    top: 61px;
    font-size: 7.6px;
    line-height: 12.2px;
    color: var(--ink);
  }
  .contact-address { left: 335px; }
  .contact-lines { left: 428px; }
  .contact-line {
    display: flex;
    align-items: center;
    gap: 5px;
  }
  .contact-icon {
    width: 7px;
    height: 7px;
    fill: var(--brand-teal);
  }
  .backdrop-circle {
    position: absolute;
    left: 0;
    top: 0;
  }
</style>
</head>
<body>
  <main class="letterhead">
    <svg class="backdrop-circle" width="541" height="763" aria-hidden="true">
      <circle cx="140" cy="585" r="170" fill="none" stroke="var(--teal-faint)" stroke-width="64"/>
    </svg>

    <header class="brand">
      <span class="brand-dot"></span>
      <span class="brand-name">Brindlemark Services Ltd</span>
    </header>

    <address class="contact contact-address" style="font-style:normal">
      412 Harlow Street<br>
      Suite 210<br>
      Fairbrook, CA 60412
    </address>

    <div class="contact contact-lines">
      <div class="contact-line">
        <svg class="contact-icon" viewBox="0 0 10 10"><path d="M2 0.5 L3.8 0.5 L4.3 3 L3 3.8 Q4 6 6.2 7 L7 5.7 L9.5 6.2 L9.5 8 Q9.5 9.5 8 9.5 Q1 9 0.5 2 Q0.5 0.5 2 0.5Z"/></svg>
        <span>555-014-2736</span>
      </div>
      <div class="contact-line">
        <svg class="contact-icon" viewBox="0 0 10 10"><path d="M0.5 2 H9.5 V8.5 H0.5Z M0.5 2 L5 5.5 L9.5 2" /></svg>
        <span>info@brindlemark.com</span>
      </div>
      <div class="contact-line">
        <svg class="contact-icon" viewBox="0 0 10 10"><circle cx="5" cy="5" r="4.2" fill="none" stroke="var(--brand-teal)" stroke-width="1"/><path d="M0.8 5 H9.2 M5 0.8 Q2.5 5 5 9.2 M5 0.8 Q7.5 5 5 9.2" fill="none" stroke="var(--brand-teal)" stroke-width="0.8"/></svg>
        <span>brindlemark.com</span>
      </div>
    </div>
  </main>
</body>
</html>
```